Marketing Postcards

I recently changed real estate companies and want to redo some advertising postcards I've used in the past. I want to replicate the existing cards with updated company info. Please see attached for proofs of old cards as well as the new company logo.

Industry/Entity Type

Real Estate

```html
<!DOCTYPE html>
<html lang="en">
<head>
<meta charset="utf-8">
<title>Marla Quinn – Marketing Postcards</title>
<link rel="stylesheet" href="https://fonts.googleapis.com/css2?family=Lato:wght@400;700&family=Oswald:wght@400;500;600&family=Roboto+Condensed:wght@700&display=swap">
<style>
  :root {
    --plum: #5b2450;
    --plum-deep: #3a1731;
    --plum-mid: #55294b;
    --ink: #1b1b1b;
    --grey: #6d6d6d;
    --paper: #ffffff;
    --backdrop: #e7e5e6;
  }
  * { box-sizing: border-box; margin: 0; padding: 0; }
  html, body { width: 1072px; height: 1200px; overflow: hidden; }
  body { background: var(--backdrop); position: relative; font-family: "Lato", sans-serif; }

  .postcard {
    position: absolute; left: 141px; width: 798px; height: 536px;
    background: var(--paper); overflow: hidden;
    box-shadow: 0 3px 10px rgba(0,0,0,.18);
  }
  .postcard--front { top: 45px; }
  .postcard--back { top: 619px; }

  .agent-header { position: absolute; left: 0; top: 0; width: 468px; height: 200px; }
  .agent-portrait {
    position: absolute; left: 21px; top: 23px; width: 110px; height: 158px;
    border: 3px solid var(--plum);
    background: linear-gradient(180deg, #e9e4e2 0%, #cdb7a6 45%, #2d4f8f 75%, #24427a 100%);
  }
  .agent-details { position: absolute; left: 149px; top: 20px; }
  .call-today { font-family: "Oswald", sans-serif; font-weight: 400; font-size: 21px; color: var(--grey); line-height: 1.1; }
  .agent-name { font-family: "Oswald", sans-serif; font-weight: 600; font-size: 25px; color: var(--plum); line-height: 1.15; margin-top: 4px; letter-spacing: .3px; }
  .agent-phone { font-family: "Oswald", sans-serif; font-weight: 500; font-size: 31px; color: var(--ink); line-height: 1.05; }
  .agent-contact { font-size: 11.5px; color: #333; line-height: 1.3; margin-top: 3px; }
  .tagline { font-family: "Roboto Condensed", sans-serif; font-weight: 700; font-size: 17px; color: var(--ink); margin-top: 6px; letter-spacing: .3px; }

  .brokerage { position: absolute; left: 318px; top: 40px; width: 140px; text-align: center; }
  .brokerage-mark { width: 34px; height: 34px; border-radius: 50%; border: 2px solid var(--plum); margin: 0 auto 6px; }
  .brokerage-name { font-family: "Oswald", sans-serif; font-weight: 500; font-size: 15px; color: var(--plum); line-height: 1.2; letter-spacing: .5px; }

  .divider { position: absolute; left: 468px; top: 0; width: 9px; height: 100%; background: var(--plum); border-left: 3px solid var(--paper); }

  .room-photo {
    position: absolute; left: 0; top: 200px; width: 468px; height: 336px;
    background: linear-gradient(180deg, #d6dadd 0%, #b7c0c6 45%, #a4acb1 62%, #3f302a 78%, #2c2220 100%);
  }
  .chevron { position: absolute; left: 0; top: 200px; width: 468px; height: 72px; }

  .message-panel {
    position: absolute; left: 477px; top: 0; width: 321px; height: 100%;
    background: linear-gradient(180deg, var(--plum-deep) 0%, var(--plum-mid) 100%);
    color: #fff; padding: 22px 22px 0 19px;
    font-size: 16.5px; line-height: 1.3; text-align: justify; hyphens: auto;
  }
  .message-panel p + p { margin-top: 14px; }

  .office-box {
    position: absolute; left: 0; top: 245px; width: 468px; height: 213px;
    background: var(--plum); color: #fff; border-radius: 0 30px 30px 0;
    padding: 14px 14px 0 33px;
  }
  .office-address { font-family: "Roboto Condensed", sans-serif; font-weight: 700; font-size: 18px; }
  .pledge-title { font-family: "Roboto Condensed", sans-serif; font-weight: 700; font-size: 15px; margin-top: 12px; }
  .pledge-text { font-size: 16px; line-height: 1.3; margin-top: 4px; }

  .back-divider { position: absolute; left: 468px; top: 0; width: 4px; height: 100%; background: var(--plum); }
  .stamp-box { position: absolute; left: 652px; top: 25px; width: 104px; height: 106px; border: 2px solid #222; }
</style>
</head>
<body>

<section class="postcard postcard--front">
  <header class="agent-header">
    <div class="agent-portrait" role="img" aria-label="Portrait photo of the agent"></div>
    <div class="agent-details">
      <p class="call-today">Call Today!</p>
      <h1 class="agent-name">MARLA QUINN</h1>
      <p class="agent-phone">555-214-0386</p>
      <p class="agent-contact">hello@marlaquinnhomes.com<br>MarlaQuinnHomes.com</p>
      <p class="tagline">With you every step of the way!</p>
    </div>
    <div class="brokerage">
      <div class="brokerage-mark"></div>
      <p class="brokerage-name">HARBOR CREST<br>REALTY</p>
    </div>
  </header>
  <div class="room-photo" role="img" aria-label="Photo of a bright living room with fireplace and dark wood floor"></div>
  <svg class="chevron" viewBox="0 0 468 72" preserveAspectRatio="none" aria-hidden="true">
    <polygon points="0,0 468,0 468,10 234,58 0,10" fill="#ffffff"/>
    <polygon points="0,10 234,58 468,10 468,22 234,70 0,22" fill="#5b2450"/>
    <polyline points="0,14 234,62 468,14" fill="none" stroke="#ffffff" stroke-width="2"/>
    <polyline points="0,8 234,56 468,8" fill="none" stroke="#1b1b1b" stroke-width="1.5"/>
  </svg>
  <div class="divider"></div>
  <article class="message-panel">
    <p>Regardless of whether you plan to sell your home this year, or perhaps down the road, it's never too soon to have a real estate market analysis. Utilize our professional expertise to maximize the return of any future improvements you might be considering.</p>
    <p>dummy text of the printing and typesetting industry. Lorem Ipsum has been the industry's standard dummy text ever since the 1500s, when an unknown printer took a galley of type and scrambled it to make a type specimen book.</p>
    <p>dummy text of the printing and typesetting industry. Lorem Ipsum has been the industry's standard dummy text ever since the 1500s,</p>
  </article>
</section>

<section class="postcard postcard--back">
  <header class="agent-header">
    <div class="agent-portrait" role="img" aria-label="Portrait photo of the agent"></div>
    <div class="agent-details">
      <p class="call-today">Call Today!</p>
      <h2 class="agent-name">MARLA QUINN</h2>
      <p class="agent-phone">555-214-0386</p>
      <p class="agent-contact">hello@marlaquinnhomes.com<br>MarlaQuinnHomes.com</p>
      <p class="tagline">With you every step of the way!</p>
    </div>
    <div class="brokerage">
      <div class="brokerage-mark"></div>
      <p class="brokerage-name">HARBOR CREST<br>REALTY</p>
    </div>
  </header>
  <div class="office-box">
    <p class="office-address">418-B Cedar Point Ave., Riverton, NC</p>
    <p class="pledge-title">Complete Confidentiality &amp; No Obligation Pledge</p>
    <p class="pledge-text">Meetings, assessments and correspondence are kept solely between the homeowner and/or the designated representative and do not require a commitment. It is our passion to respond promptly to real estate questions and see creative solutions no matter how great the vision.</p>
  </div>
  <div class="back-divider"></div>
  <div class="stamp-box"></div>
</section>

</body>
</html>
```